Sell Sheet for Food Topping Applicator Manufacturer, Primarily Frozen Pizza, Tray Meals, Bakery i...

Sell sheet-2 sided w front showing machine photo, sell points. Back page listing some specs and technical information/photos. RVKD8 attachment shows what we currently have - we are looking for a new, fresh look.
We like the look of the file attached, Pellman Cascade Topping Dispenser, so we'd like something with this clean look.

Target Market(s)

Food Processing Industry

Industry/Entity Type

Machinery

Font styles to use
Serif

Colors
3176b5

Requirements
Must have
• Should be clean looking. Our logo present. Selling points, possibly in paragraph form on front, Back page to have specs, some drawings of machine. We currently use blue, gray, white and black colors.

```html
<!DOCTYPE html>
<html lang="en">
<head>
<meta charset="utf-8">
<title>Sauce Applicator Sell Sheet</title>
<link href="https://fonts.googleapis.com/css2?family=Exo+2:wght@300;400;800;900&family=Lato:wght@300;400;700&display=swap" rel="stylesheet">
<style>
  :root{
    --blue:#2f55f0;
    --blue-deep:#2444d6;
    --blue-text:#2a4fe8;
    --gray-tab:#6d6d6f;
    --panel:#f1f1f3;
    --ink:#4a4a4a;
    --backdrop:#bdbdbd;
    --white:#ffffff;
    --photo-a:#8a8e96;
    --photo-b:#d8dbe0;
  }
  *{box-sizing:border-box;margin:0;padding:0}
  html,body{width:703px;height:1200px;overflow:hidden}
  body{background:var(--backdrop);font-family:"Lato",sans-serif;color:var(--ink);position:relative}
  .page{position:absolute;left:131px;width:440px;height:572px;background:var(--white);overflow:hidden}
  .page--front{top:18px}
  .page--back{top:610px}
  .abs{position:absolute}
  .on-top{z-index:3}

  /* front */
  .hero{left:0;top:0;width:440px;height:208px;background:linear-gradient(135deg,#2a4de8 0%,#3560f4 55%,#2f55ee 100%)}
  .hero-kicker{left:25px;top:28px;font-family:"Exo 2",sans-serif;font-weight:300;font-size:15px;color:var(--white);letter-spacing:.3px}
  .hero-title{left:21px;top:44px;font-family:"Exo 2",sans-serif;font-weight:900;color:var(--white);line-height:.9}
  .hero-title .big{display:block;font-size:53px;letter-spacing:.5px}
  .hero-title .sub{display:block;font-size:28.5px;letter-spacing:.6px;margin-top:3px}
  .hero-copy{left:22px;top:126px;width:182px;font-size:6.1px;line-height:1.3;color:var(--white)}
  .model-band{left:140px;top:182px;width:300px;height:26px;background:var(--blue-deep);clip-path:polygon(22px 0,100% 0,100% 100%,0 100%)}
  .model-label{left:154px;top:188px;font-family:"Lato",sans-serif;font-size:11px;color:var(--white);letter-spacing:.3px}
  .spec-tab{left:0;top:208px;width:130px;height:25px;background:var(--gray-tab);clip-path:polygon(0 0,100% 0,82% 100%,0 100%)}
  .spec-tab span{position:absolute;left:22px;top:7px;font-family:"Exo 2",sans-serif;font-weight:800;font-size:9px;color:var(--white);letter-spacing:.3px}
  .machine-photo{left:248px;top:9px;width:160px;height:272px;border-radius:40px 40px 10px 10px;background:linear-gradient(160deg,var(--photo-b) 0%,var(--photo-a) 60%,#5d6068 100%)}
  .spec-col{left:22px;top:244px;width:205px}
  .spec h3{font-family:"Exo 2",sans-serif;font-weight:800;font-size:7.4px;color:var(--blue-text);letter-spacing:.2px;margin-bottom:2px}
  .spec p{font-size:5.6px;line-height:1.35;margin-bottom:7px}
  .rate-table{border-collapse:collapse;font-size:5.6px;margin:2px 0 9px;border:0.6px solid #999}
  .rate-table td{padding:1px 3px;line-height:1.3}
  .rate-table .mid{border-right:0.6px solid #999;padding-right:12px}
  .inline-spec{display:flex;gap:6px;align-items:baseline;margin-bottom:7px}
  .inline-spec h3{margin:0}
  .inline-spec p{margin:0}
  .spec-panel{left:241px;top:287px;width:163px;height:236px;background:var(--panel);padding:10px 12px}
  .logo-word{left:22px;top:530px;width:140px;height:24px;display:flex;align-items:center;justify-content:center;gap:6px;font-family:"Exo 2",sans-serif;font-weight:400;font-size:15px;letter-spacing:3px;color:var(--blue-deep)}
  .logo-dot{width:7px;height:7px;border-radius:50%;background:var(--blue-deep)}
  .foot-stripe{left:180px;top:515px;width:260px;height:8px;background:var(--gray-tab);clip-path:polygon(14px 0,100% 0,100% 100%,6px 100%)}
  .foot-band{left:186px;top:521px;width:254px;height:51px;background:var(--blue);clip-path:polygon(24px 0,100% 0,100% 100%,0 100%)}
  .foot-url{left:257px;top:537px;font-family:"Lato",sans-serif;font-weight:300;font-size:12.5px;letter-spacing:1.4px;color:var(--white)}

  /* back */
  .drawing{background:linear-gradient(180deg,#f7f7f8,#ececee);border:0.6px solid #d6d6d8}
  .drawing-a{left:12px;top:20px;width:148px;height:112px}
  .drawing-b{left:170px;top:24px;width:70px;height:104px}
  .drawing-c{left:12px;top:161px;width:148px;height:148px}
  .drawing-d{left:182px;top:168px;width:62px;height:141px}
  .gallery{left:274px;top:23px;width:146px}
  .shot{position:absolute;width:70px}
  .shot .frame{width:70px;height:81px;border:1.2px solid #3a3a3a;background:linear-gradient(160deg,#c9ccd2,#7b7f88)}
  .shot .frame.blue{background:linear-gradient(160deg,#d2d5da 0%,#8a8e96 45%,#3b63e8 100%)}
  .shot p{font-size:4.6px;line-height:1.2;text-align:center;margin-top:2px}
  .back-band{left:0;top:450px;width:440px;height:122px;background:var(--blue)}
  .back-machine{left:30px;top:313px;width:172px;height:246px;border-radius:36px 36px 10px 10px;background:linear-gradient(160deg,var(--photo-b) 0%,var(--photo-a) 60%,#5d6068 100%)}
  .back-pitch{right:28px;top:465px;width:192px;text-align:right;font-family:"Exo 2",sans-serif;font-weight:800;font-size:7.2px;line-height:1.3;color:var(--white);letter-spacing:.2px}
  .back-call{right:28px;top:518px;font-size:9.4px;color:var(--white)}
  .back-contact{right:28px;top:539px;font-size:9.2px;color:var(--white);white-space:nowrap}
</style>
</head>
<body>

<section class="page page--front">
  <div class="abs hero"></div>
  <div class="abs hero-kicker">CONVEYORIZED PRECISION</div>
  <h1 class="abs hero-title"><span class="big">SAUCE</span><span class="sub">APPLICATOR</span></h1>
  <p class="abs hero-copy">USDA compliant, patented sauce applicator, capable of evenly applying sauce to your product while maintaining a sauce free border. Our CONVEYORIZED PRECISION sauce applicator is a simple easy to use system. Your pizzas are precisely located under the applicating head by means of our conveyor. When in position, the sauce is automatically applied.</p>
  <div class="abs model-band"></div>
  <div class="abs machine-photo" role="img" aria-label="Photo of the stainless steel sauce applicator with conical hopper and blue conveyor belt"></div>
  <div class="abs model-label on-top">MODEL #RVKD8</div>
  <div class="abs spec-tab"><span>SPECIFICATIONS</span></div>

  <div class="abs spec-col">
    <div class="spec"><h3>Products</h3><p>Rigid and Supported Products Square, Rectangular, and Round<br>Up To 18"</p></div>
    <div class="spec"><h3>SAUCE:</h3><p>Flowable Product with All Particulate Able to Pass Through a 5/32" (2mm) Diameter Hole Screen. Larger Particulates Possible on Custom Designed Patterns</p></div>
    <div class="spec"><h3>PRODUCTION RATES (CP To):</h3>
      <table class="rate-table">
        <tr><td>6"</td><td>@</td><td class="mid">110+ Pizzas Per Minute,</td><td>6,600+ Per Hour</td></tr>
        <tr><td>8"</td><td>@</td><td class="mid">110+ Pizzas Per Minute,</td><td>6,600+ Per Hour</td></tr>
        <tr><td>10"</td><td>@</td><td class="mid">96 Pizzas Per Minute,</td><td>5,760 Per Hour</td></tr>
        <tr><td>12"</td><td>@</td><td class="mid">80 Pizzas Per Minute,</td><td>4,800 Per Hour</td></tr>
        <tr><td>14"</td><td>@</td><td class="mid">68 Pizzas Per Minute,</td><td>4,080 Per Hour</td></tr>
        <tr><td>16"</td><td>@</td><td class="mid">60 Pizzas Per Minute,</td><td>3,600 Per Hour</td></tr>
      </table>
    </div>
    <div class="spec"><h3>ELECTRICAL:</h3><p>220 Volts, 1 Phase, 5 Amp Circuit, 60 Hz, Stainless Steel Control Enclosure</p></div>
    <div class="spec inline-spec"><h3>PNEUMATIC:</h3><p>80 PSIG @ 6 SCFM &nbsp;&nbsp; Clean Dry Air</p></div>
    <div class="spec"><h3>OPTIONS:</h3><p>Hopper Level Pump and Level Control. Dual Lanes for Smaller Products. Start/Stop Interconnectivity, Stainless Steel Conical Hopper</p></div>
  </div>

  <div class="abs spec-panel">
    <div class="spec"><h3>PORTION:</h3><p>0.5 oz. (14 g) to 10 oz. (284g) +/- 0.2 oz. (6 g)</p></div>
    <div class="spec"><h3>HOPPER:</h3><p>12 Gallon Hopper (45.4 liters) (approx.)</p></div>
    <div class="spec"><h3>STANDARD PATTERNS:</h3><p>0.5 in. (12.7mm) Increments<br>Custom Patterns Also Available</p></div>
    <div class="spec"><h3>CONTROLS:</h3><p>7" Color Touch Screen</p></div>
    <div class="spec"><h3>DRIVE SYSTEM:</h3><p>conveyor Utilizes a Precision Electric Drive Motor<br>Washdown Capable</p></div>
    <div class="spec"><h3>CANTILEVERED CONVEYOR:</h3><p>conveyor Utilizes a Precision Electric Drive Motor<br>Washdown Capable</p></div>
    <div class="spec"><h3>FRAME:</h3><p>Stainless Steel Frame<br>Locking Swivel Casters with No Exposed Threads</p></div>
  </div>

  <div class="abs logo-word"><span>MERIDIAN</span><span class="logo-dot"></span></div>
  <div class="abs foot-stripe"></div>
  <div class="abs foot-band"></div>
  <div class="abs foot-url">WWW.MRD-TS.COM</div>
</section>

<section class="page page--back">
  <div class="abs drawing drawing-a" role="img" aria-label="Dimensioned front elevation drawing of the applicator"></div>
  <div class="abs drawing drawing-b" role="img" aria-label="Isometric line drawing of the applicator frame"></div>
  <div class="abs drawing drawing-c" role="img" aria-label="Dimensioned side elevation drawing with hopper"></div>
  <div class="abs drawing drawing-d" role="img" aria-label="Dimensioned end elevation drawing"></div>

  <div class="abs gallery">
    <div class="shot" style="left:0;top:0"><div class="frame" role="img" aria-label="Photo of hopper level sensor"></div><p>Hopper Level Sensor<br>(Optional)</p></div>
    <div class="shot" style="left:76px;top:0"><div class="frame blue" role="img" aria-label="Photo of belt removal"></div><p>No Tool Required<br>Belt Removal</p></div>
    <div class="shot" style="left:0;top:112px"><div class="frame" role="img" aria-label="Photo of color touch panel"></div><p>7" Color Panel View<br>with Color Stack Light</p></div>
    <div class="shot" style="left:76px;top:112px"><div class="frame blue" role="img" aria-label="Photo of adjustable lane guide"></div><p>Floating, Adjustable<br>Lane Guide</p></div>
    <div class="shot" style="left:0;top:216px"><div class="frame" role="img" aria-label="Photo of transfer pump"></div><p>Transfer Pump<br>(Optional)</p></div>
    <div class="shot" style="left:76px;top:216px"><div class="frame" role="img" aria-label="Photo of locking caster"></div><p>Heavy Duty Locking Casters<br>with No Exposed Threads</p></div>
    <div class="shot" style="left:0;top:321px"><div class="frame" role="img" aria-label="Photo of caster detail"></div><p>Heavy Duty Locking Casters<br>with No Exposed Threads</p></div>
    <div class="shot" style="left:76px;top:321px"><div class="frame blue" role="img" aria-label="Photo of cantilevered conveyor"></div><p>Removable Cantilevered<br>Conveyor</p></div>
  </div>

  <div class="abs back-band"></div>
  <div class="abs back-machine" role="img" aria-label="Photo of the complete sauce applicator machine"></div>
  <p class="abs back-pitch on-top">MERIDIAN MANUFACTURES HIGH SPEED AUTOMATED TOPPING EQUIPMENT. WE OFFER STANDARD PRODUCTION SYSTEMS AS WELL AS CUSTOM ENGINEERED SOLUTIONS.</p>
  <p class="abs back-call on-top">CALL US NOW 1815.555.0182</p>
  <p class="abs back-contact on-top">INFO@MRD-TS.COM &nbsp;|&nbsp; WWW.MRD-TS.COM</p>
</section>

</body>
</html>
```